Business Card Design

We are an all natural, organic, salon and spa. I have bought cards on here and have an account. I love the designs that can be simple but at the same time have vines or green leaves, lady profile etc. but not too much. Our name is quite lengthy and it does take up space. I want the slogan: Beauty...inspired by nature! to be on the card somewhere if possible. We also have an Eco friendly boutique and retail organic products.
We need the back side for appointment information. Our lighted box sign has 3 leaves sprouting but was considering changing to have all match even on our website so we can brand our name and logo.
We are classy but down to earth at the same time. If you need to look at our account at old cards or go to our website at www.bramblecovehairstudio.com to see some pictures and get a feel of what we look like that would be great.
I am tired of looking around trying to find what is best for us. I need this done pretty soon as I am in need of cards really soon. I can order a box of what we use now if need be. I want whatever we have to be ours to use and not copied.

Target Market(s)

Women of middle age to 60's plus. and health conscious, cancer survivors or presently going through.

Industry/Entity Type

Boutique

Contact Information for Business Card

Willowmere Organic Salon & Spa Slogan branding: Beauty...inspired by nature!
2917 W. Harlow Crest Bvld. Suite 318
Fernhaven, Fl. 35821
352-718-4096
www.bramblecovehairstudio.com

Colors
acd036
9bcb3c
cadf82

Requirements
Must have
• Fonts that are more organic looking on our sign, but please give me options
Hair or lady's face, profile etc. Has to convey it's a salon and spa by seeing the logo.
Green color fonts for our name. Maybe another color somewhere...lips of color to go with the apple green...etc.
Backside has to have appointment schedule
Nice to have

Should not have
• Clients should not think of this place as an herbal supplement store so we need something that says salon and spa.

```html
<!DOCTYPE html>
<html lang="en">
<head>
<meta charset="utf-8">
<title>Willowmere Organic Salon &amp; Spa – Business Card</title>
<link href="https://fonts.googleapis.com/css2?family=Encode+Sans+Condensed:wght@300;400&family=Yellowtail&display=swap" rel="stylesheet">
<style>
  :root{
    --backdrop:#f2edc1;
    --card-left:#e0ebe9;
    --lime-pale:#cadf82;
    --lime:#9bcb3c;
    --lime-strong:#9bc43c;
    --forest:#4a7f2e;
    --forest-dark:#3f7229;
    --teal-green:#3a9368;
    --icon-green:#2f8a5a;
    --logo-disc:#a6cf4c;
    --tag-paper:#ebe3d3;
    --ink:#1d1d1d;
    --white:#ffffff;
  }
  *{margin:0;padding:0;box-sizing:border-box;}
  html,body{width:1200px;height:1000px;overflow:hidden;}
  body{
    background:var(--backdrop);
    position:relative;
    font-family:"Encode Sans Condensed", "Arial Narrow", sans-serif;
    font-weight:300;
  }

  /* side tag */
  .side-tag{
    position:absolute;left:30px;top:255px;width:140px;height:126px;
    background:var(--tag-paper);
    box-shadow:0 4px 8px rgba(0,0,0,.12);
  }
  .side-tag__holes{position:absolute;left:7px;top:4px;display:flex;gap:11px;}
  .side-tag__holes span{width:12px;height:12px;border-radius:50%;background:var(--backdrop);}
  .side-tag__label{
    position:absolute;left:24px;top:52px;
    font-family:"Yellowtail", "Brush Script MT", cursive;font-size:31px;color:var(--ink);
  }

  /* card */
  .card{
    position:absolute;left:170px;top:100px;width:811px;height:450px;
    display:flex;
  }
  .card__front{
    position:relative;width:405px;height:450px;background:var(--card-left);
  }
  .card__back{
    position:relative;width:406px;height:450px;background:var(--lime-pale);
    box-shadow:-10px 0 14px rgba(0,0,0,.18);
  }

  .brand-mark{
    position:absolute;left:118px;top:55px;width:178px;height:178px;
    border-radius:50%;background:var(--logo-disc);
  }
  .brand-name{
    position:absolute;left:0;top:270px;width:405px;text-align:center;
    color:var(--teal-green);font-weight:300;line-height:1;
  }
  .brand-name__main{display:block;font-size:44px;}
  .brand-name__sub{display:block;font-size:38px;margin-top:4px;}

  .website{
    position:absolute;left:14px;top:415px;display:flex;align-items:center;gap:12px;
    color:var(--teal-green);font-size:28px;
  }
  .website__icon{width:18px;height:18px;}

  .stripe{position:absolute;left:0;width:406px;}
  .stripe--a{top:52px;height:13px;background:var(--lime-strong);}
  .slogan-band{
    position:absolute;left:0;top:94px;width:406px;height:49px;
    background:var(--forest);color:var(--white);
    font-size:36px;line-height:49px;padding-left:17px;white-space:nowrap;
  }
  .stripe--b{top:160px;height:25px;background:var(--lime);}
  .stripe--c{top:185px;height:13px;background:linear-gradient(90deg,var(--lime-strong),var(--forest-dark) 40%,var(--forest-dark));}
  .stripe--d{top:198px;height:92px;background:var(--lime);}
  .stripe--e{top:297px;height:16px;background:var(--lime-strong);}
  .stripe--f{top:324px;height:9px;left:3px;width:406px;background:linear-gradient(90deg,var(--lime-strong),var(--forest-dark) 50%);}

  .contact{position:absolute;left:0;top:338px;color:var(--teal-green);font-size:28px;line-height:38px;}
  .contact__row{display:flex;align-items:flex-start;}
  .contact__icon{width:73px;display:flex;justify-content:center;padding-top:8px;}
  .contact__row--phone .contact__icon{padding-top:6px;}
</style>
</head>
<body>

  <div class="side-tag">
    <div class="side-tag__holes"><span></span><span></span><span></span><span></span><span></span><span></span></div>
    <div class="side-tag__label">Front</div>
  </div>

  <div class="card">
    <section class="card__front">
      <div class="brand-mark" aria-hidden="true"></div>
      <h1 class="brand-name">
        <span class="brand-name__main">Willowmere</span>
        <span class="brand-name__sub">Organic Salon &amp; Spa</span>
      </h1>
      <div class="website">
        <svg class="website__icon" viewBox="0 0 18 18" aria-hidden="true">
          <circle cx="9" cy="9" r="8.5" fill="var(--teal-green)"/>
          <path d="M5 5c2 0 3 2 2 3s-2 2-1 4M11 3c0 2 2 2 3 3M12 11c1 1 1 3 0 4" stroke="var(--card-left)" stroke-width="1.6" fill="none"/>
        </svg>
        <span>www.bramblecovehairstudio.com</span>
      </div>
    </section>

    <section class="card__back">
      <div class="stripe stripe--a"></div>
      <div class="slogan-band">Beauty...inspired by nature!</div>
      <div class="stripe stripe--b"></div>
      <div class="stripe stripe--c"></div>
      <div class="stripe stripe--d"></div>
      <div class="stripe stripe--e"></div>
      <div class="stripe stripe--f"></div>

      <div class="contact">
        <div class="contact__row">
          <div class="contact__icon">
            <svg width="34" height="30" viewBox="0 0 34 30" aria-hidden="true">
              <path d="M17 1 1 15h5v14h8v-9h6v9h8V15h5z" fill="var(--icon-green)"/>
            </svg>
          </div>
          <div>2917 W. Harlow Crest Bvld.<br>Suite 318 Fernhaven, FL.</div>
        </div>
        <div class="contact__row contact__row--phone">
          <div class="contact__icon">
            <svg width="16" height="26" viewBox="0 0 16 26" aria-hidden="true">
              <rect x="1" y="1" width="14" height="24" rx="2.5" fill="none" stroke="var(--icon-green)" stroke-width="2"/>
              <rect x="3.5" y="4" width="9" height="14" fill="var(--icon-green)"/>
              <circle cx="8" cy="21.5" r="1.4" fill="var(--icon-green)"/>
            </svg>
          </div>
          <div>418-718-4096 35821</div>
        </div>
      </div>
    </section>
  </div>

</body>
</html>
```